Web Design for Harbor Ledger Allies

Harbor Ledger Allies needs the photoshop files for a simple, clean and professional website design. The company is building a network of bookkeepers/accountants to handle outsourced bookkeeping services for start ups and small businesses. It needs to both attract bookkeepers to become partners and give clients confidence in the professional network. The partners will use products like Tallymint Web, Brightfolio.example and PennyTrim.example for start ups, as well as help with tasks using the clients existing accounting software.

A home and subpage design is needed. I'll award the work based on the home design. The minor subpage changes can be worked out in the workroom stage.

The pages for the navigation will be: Home, Services, Locations, Partners, FAQ, Contact

```html
<!DOCTYPE html>
<html lang="en">
<head>
<meta charset="utf-8">
<title>Harbor Ledger Allies – Outsourced Bookkeeping</title>
<link rel="stylesheet" href="https://fonts.googleapis.com/css2?family=Open+Sans:wght@400;600;700;800&display=swap">
<style>
  :root {
    --blue: #2a9fd8;
    --blue-dark: #1b7fb3;
    --ink: #2b2b2b;
    --text: #5a5a5a;
    --muted: #9a9a9a;
    --line: #d9d9d9;
    --panel: #e7e8e9;
    --footer: #1f2021;
    --white: #ffffff;
  }
  * { box-sizing: border-box; margin: 0; padding: 0; }
  html, body { width: 859px; height: 1200px; overflow: hidden; }
  body { background: var(--white); font-family: "Open Sans", Arial, sans-serif; color: var(--text); position: relative; }

  .site-header { height: 115px; display: flex; align-items: flex-end; justify-content: space-between; padding: 0 72px 14px 86px; }
  .brand { display: flex; align-items: center; gap: 10px; }
  .brand-square { width: 14px; height: 14px; background: var(--blue); }
  .brand-name { font-size: 17px; font-weight: 700; color: var(--blue); letter-spacing: .5px; line-height: 1; text-transform: uppercase; }
  .main-nav { display: flex; align-items: center; font-size: 13px; font-weight: 700; color: var(--ink); padding-bottom: 4px; }
  .main-nav a { color: inherit; text-decoration: none; padding: 0 10px; border-left: 1px solid var(--ink); line-height: 1; }
  .main-nav a:first-child { border-left: 0; }
  .main-nav a.is-active { color: var(--blue); text-decoration: underline; text-underline-offset: 4px; }

  .hero { position: relative; margin: 0 72px 0 86px; height: 322px; overflow: hidden; }
  .hero-photo { position: absolute; inset: 0; background: radial-gradient(ellipse at 38% 35%, #f4f7f9 0%, #c9d3da 45%, #7d8d99 100%); }
  .hero-headline { position: absolute; right: 0; top: 118px; text-align: left; }
  .hero-headline span { display: block; font-weight: 800; font-size: 24px; line-height: 1.1; color: var(--white); text-transform: uppercase; padding: 4px 16px; background: rgba(30, 40, 48, .78); }
  .hero-headline span.accent { background: var(--blue); }
  .slider-dots { position: absolute; right: 18px; bottom: 10px; display: flex; gap: 4px; }
  .slider-dots i { width: 14px; height: 4px; background: rgba(255,255,255,.55); }
  .slider-dots i.on { background: var(--blue); }

  .content { display: flex; gap: 26px; margin: 38px 72px 0 86px; }
  .feature { width: 218px; }
  .feature h2 { display: flex; align-items: center; gap: 8px; font-size: 17px; font-weight: 800; color: var(--ink); text-transform: uppercase; margin-bottom: 14px; }
  .feature h2 em { font-style: normal; color: var(--blue); }
  .feature p { font-size: 10.5px; line-height: 1.45; margin-bottom: 8px; }
  .view-more { display: flex; align-items: center; gap: 6px; font-size: 10px; font-weight: 700; color: var(--ink); text-decoration: none; margin-top: 14px; }
  .view-more svg { width: 12px; height: 8px; }

  .consult-form { width: 222px; margin-left: auto; background: var(--panel); padding: 14px 14px 16px; border: 1px solid var(--line); }
  .consult-form h3 { text-align: center; font-size: 18px; font-weight: 800; color: var(--ink); line-height: 1.05; }
  .consult-form .sub { text-align: center; font-size: 11px; font-weight: 700; color: var(--blue); text-transform: uppercase; margin-bottom: 12px; }
  .field { background: var(--white); border: 1px solid var(--line); height: 22px; font-size: 9px; color: var(--muted); padding: 5px 6px; margin-bottom: 7px; }
  .field-row { display: flex; gap: 6px; }
  .field-row .field { flex: 1; }
  .field.tall { height: 62px; }
  .submit { display: block; margin: 8px auto 0; width: 90px; height: 22px; border: 0; background: var(--blue); color: var(--white); font-family: inherit; font-size: 10px; font-weight: 700; }

  .software { margin: 52px 72px 0 86px; }
  .software h2 { display: flex; align-items: center; gap: 14px; font-size: 18px; font-weight: 800; color: var(--ink); text-transform: uppercase; }
  .software h2::before, .software h2::after { content: ""; flex: 1; height: 10px; background: #ececec; }
  .software-list { display: flex; justify-content: space-around; align-items: center; margin-top: 34px; }
  .software-name { font-size: 17px; font-weight: 700; color: var(--ink); }

  .site-footer { position: absolute; left: 0; right: 0; bottom: 0; height: 120px; background: var(--footer); display: flex; align-items: center; padding: 0 72px 0 146px; gap: 40px; }
  .site-footer .brand-name { font-size: 14px; }
  .footer-links { display: flex; font-size: 10px; color: #cfcfcf; border-left: 1px solid #555; padding-left: 14px; }
  .footer-links a { color: inherit; text-decoration: none; padding: 0 9px; border-left: 1px solid #777; line-height: 1; }
  .footer-links a:first-child { border-left: 0; padding-left: 0; }
  .footer-copy { font-size: 8.5px; color: #8a8a8a; margin-top: 8px; padding-left: 14px; border-left: 1px solid #555; }
</style>
</head>
<body>
  <header class="site-header">
    <div class="brand">
      <span class="brand-square"></span>
      <span class="brand-name">Harbor Ledger Allies</span>
    </div>
    <nav class="main-nav">
      <a href="#">HOME</a><a href="#">SERVICES</a><a href="#" class="is-active">LOCATIONS</a><a href="#">PARTNERS</a><a href="#">FAQ</a><a href="#">CONTACT</a>
    </nav>
  </header>

  <section class="hero">
    <div class="hero-photo" role="img" aria-label="Photo of a hand touching a glowing cloud network connecting laptop, phone and mail icons"></div>
    <h1 class="hero-headline">
      <span>Outsourced</span>
      <span>Bookkeeping</span>
      <span>Services for</span>
      <span class="accent">Small Businesses</span>
    </h1>
    <div class="slider-dots"><i class="on"></i><i></i><i></i></div>
  </section>

  <main class="content">
    <article class="feature">
      <h2>
        <svg width="26" height="26" viewBox="0 0 26 26"><circle cx="10" cy="15" r="7" fill="none" stroke="#555" stroke-width="3" stroke-dasharray="3 2"/><circle cx="10" cy="15" r="2.5" fill="#555"/><circle cx="19" cy="7" r="4.5" fill="none" stroke="#2a9fd8" stroke-width="2.5" stroke-dasharray="2 1.5"/></svg>
        Our <em>Services</em>
      </h2>
      <p>Lorem ipsum dolor sit amet, consectetur adipiscing elit. Mauris fringilla nibh vel neque fringilla, quis mattis lorem condimentum. Etiam rhoncus faucibus eros ut egestas. Nulla nulla est, congue in semper vitae, blandit eget mi.</p>
      <p>Nam posuere laoreet eros in cursus. Vivamus pharetra justo ac risus hendrerit sodales.</p>
      <a class="view-more" href="#"><svg viewBox="0 0 12 8"><path d="M0 4h10M7 1l3 3-3 3" stroke="#2a9fd8" stroke-width="1.6" fill="none"/></svg>VIEW MORE</a>
    </article>

    <article class="feature">
      <h2>
        <svg width="28" height="26" viewBox="0 0 28 26"><path d="M8 6a8 8 0 0 1 12 0M10.5 9a4.5 4.5 0 0 1 7 0" stroke="#2a9fd8" stroke-width="2" fill="none"/><circle cx="9" cy="15" r="3" fill="#555"/><circle cx="19" cy="15" r="3" fill="#555"/><path d="M3 25a6 6 0 0 1 12 0zM13 25a6 6 0 0 1 12 0z" fill="#555"/></svg>
        Become a <em>Partner</em>
      </h2>
      <p>Lorem ipsum dolor sit amet, consectetur adipiscing elit. Mauris fringilla nibh vel neque fringilla, quis mattis lorem condimentum. Etiam rhoncus faucibus eros ut egestas.</p>
      <p>Nam posuere laoreet eros in cursus. Vivamus pharetra justo ac risus hendrerit sodales.</p>
      <a class="view-more" href="#"><svg viewBox="0 0 12 8"><path d="M0 4h10M7 1l3 3-3 3" stroke="#2a9fd8" stroke-width="1.6" fill="none"/></svg>VIEW MORE</a>
    </article>

    <form class="consult-form">
      <h3>CONTACT US</h3>
      <p class="sub">for a free consultation</p>
      <div class="field">Name *</div>
      <div class="field">Email *</div>
      <div class="field">Phone</div>
      <div class="field-row"><div class="field">City</div><div class="field">State</div></div>
      <div class="field tall">Message</div>
      <button class="submit" type="button">SUBMIT</button>
    </form>
  </main>

  <section class="software">
    <h2>Software We Use</h2>
    <div class="software-list">
      <span class="software-name">Brightfolio</span>
      <span class="software-name">PennyTrim</span>
      <span class="software-name">Ovalcount</span>
      <span class="software-name">Tallymint Web</span>
    </div>
  </section>

  <footer class="site-footer">
    <div class="brand">
      <span class="brand-square"></span>
      <span class="brand-name">Harbor Ledger Allies</span>
    </div>
    <div>
      <nav class="footer-links">
        <a href="#">HOME</a><a href="#">SERVICES</a><a href="#">LOCATIONS</a><a href="#">PARTNERS</a><a href="#">FAQ</a><a href="#">CONTACT</a>
      </nav>
      <p class="footer-copy">© 2014 HARBOR LEDGER ALLIES. ALL RIGHTS RESERVED.</p>
    </div>
  </footer>
</body>
</html>
```